Colourful Bold Design for Pet Insurance Website

PLEASE NOTE THAT THIS PROJECT HAS BEEN EXTENDED. Please read the PROJECT EXTENSION DOCUMENT BEFORE STARTING WORK ON ANY DESIGNS.

We are looking for a colourful bold new template design for our JOOMLA HOMEPAGE and a matching design for our new WORDPRESS BLOG.

The website will help pet owners work out which insurance policy best meets their needs. The aim of the website is to explain policy differences in a plain clear manner.

The website will need to have a professional colourful image. It needs to be BOLD, CLEAN AND SHARP rather than soft, pastel and cuddly.

COLOUR SCHEME
The website needs to have a bold colourful design on a white background.
On the inner pages we will have five different types of policies which will be colour coded. We would ideally therefore like to incorporate five distinct colours in the design. See attached document for example of colour schemes we like.

LOGO
We want to keep the existing logo. Please find the file attached. You may though change the logo colours.

CONTENT
One of the reasons for the new design is that we want to change the style of the homepage and include new content. Our current homepage can be found at www.cover-compare-quizzo.co.uk.

Content Required
Slideshow
Article Intro.. About Pet Insurance
Policy Lookup Box (see existing site… you can change the design of this)
Six link options (see links on left of current page)
Latest Reviews (List of 6)
Ad (Same dimensions as currently on homepage)

News and Comment Section - To include Three or Four Articles, Title, Intro to article (probably 3 or 4 lines .. about 400px wide), Read more link
Social Media Section
Friendwall Plugin with Feed
Latest Tweets Plugin
Pet Charities Latest Tweets
Footer
Larger footer with lots of links grouped in sections

It does not need to include the clipart pic of the pets which is on the current homepage.

Examples of Websites and Templates We Like
http://www.brindlevox.com/ (like colours… fonts…layout)
http://layoutdemo.quarnofield.com/?template=elated&path=/... (like the clarity, "white" space etc)
http://www.skellpravo.com/demo/58817.html (like white space, clear easy to read fonts… don’t like colour scheme, size of top picture)
http://www.skellpravo.com/website-templates/62391.html (like colour scheme, use of white space)

FEEDBACK
I will provide lots of feedback on all designs submitted so that together we can get the best result.

For clarification this is a DESIGN ONLY project. Our website developer will view the designs before we make our final choice as he wants to ensure he can develop "sharp, practical and most importantly light weight web interface" from the design.

Just updated this brief to clarify design issues, content issues and to give some more examples of site designs I like. 

Please note that although we wish to keep the logo you can change the colours to suit your design. 

Please note that we have now added details of pictures we would be happy to use on the website.  We would prefer it if you used one of these.   Otherwise please ensure your picture includes a nice dog and nice cat and no people!

I have been delighted with the quality of the designs submitted for this project.  So much so that I am going to extend the project to include some additional inner pages.   The amended brief will be posted on here on Friday 10 May.   The deadline will be extended and the budget will also be increased. 

Reason: Additional inner pages now required. Budget will be increased. Revised brief to be posted on here Friday 10 May.

Target Market(s)

Pet owners in the UK who are confused about pet insurance. It therefore needs to be a bold design which is plain, clean and easy to read. It should use bold colours rather than pastels and should not use "cuddly" images.

Industry/Entity Type

Insurance

Requirements
Must have
• Bold clear and distinct colours (preferably 5)
Content as per uploaded file (not just content from existing site)
Easy to read fonts
Should not have
• Pastel colours
Cuddly images

```html
<!DOCTYPE html>
<html lang="en">
<head>
<meta charset="utf-8">
<title>Cover Compare Quizzo UK – Footer</title>
<link rel="stylesheet" href="https://fonts.googleapis.com/css2?family=Ubuntu:wght@400;500&family=Arimo:wght@400;700&display=swap">
<style>
:root{
  --page:#737373;
  --rule:#8e8e8e;
  --white:#ffffff;
  --tweet-blue:#0ab4e6;
  --tweet-teal:#00e0c8;
  --avatar-icon-blue:#2cc3ee;
  --avatar-icon-teal:#17e0cb;
  --fb-head:#edeff4;
  --fb-line:#d8dfea;
  --fb-name:#3b5998;
  --fb-text:#333333;
  --fb-muted:#777777;
  --thumb-a:#6f6a64;
  --thumb-b:#3d3a3a;
}
*{box-sizing:border-box;margin:0;padding:0}
html,body{width:1200px;height:567px;overflow:hidden;background:var(--page)}
body{position:relative;font-family:"Arimo",Arial,sans-serif;color:var(--white)}
.heading{position:absolute;top:28px;font-family:"Ubuntu",sans-serif;font-weight:500;font-size:17px;color:var(--white)}
.panel{position:absolute;top:66px;width:276px;height:271px}
/* social widget */
.fb{left:154px;background:var(--white);border:1px solid #bdc7d8;color:var(--fb-text)}
.fb-head{height:30px;background:var(--fb-head);border-bottom:1px solid #c4cde0;font-weight:700;font-size:12px;padding:8px 9px}
.fb-page{position:relative;height:60px;border-bottom:1px solid var(--fb-line);margin:0 5px}
.fb-mark{position:absolute;left:5px;top:10px;width:38px;height:38px;background:#6d84b4}
.fb-name{position:absolute;left:56px;top:9px;font-weight:700;font-size:13px;color:var(--fb-name)}
.fb-like{position:absolute;left:56px;top:30px;border:1px solid #cad4e7;background:#eceef5;border-radius:2px;font-size:10px;padding:3px 5px;color:#3b5998}
.fb-count{font-size:10px;padding:6px 10px 4px}
.fb-grid{display:grid;grid-template-columns:repeat(5,47px);column-gap:5px;row-gap:4px;padding:0 10px}
.fb-fan{text-align:center;font-size:8px;color:var(--fb-muted)}
.fb-thumb{display:block;width:47px;height:47px;background:linear-gradient(160deg,var(--thumb-a),var(--thumb-b));margin-bottom:4px}
.fb-thumb.light{background:linear-gradient(160deg,#dfe3ea,#b9c0cc)}
.fb-foot{position:absolute;left:0;right:0;bottom:0;height:21px;border-top:1px solid var(--fb-line);font-size:8px;color:#555;padding:5px 9px;display:flex;align-items:center;gap:5px}
.fb-foot i{width:12px;height:12px;background:var(--fb-name)}
/* tweet lists */
.tweets{padding-top:19px}
.tweets.latest{left:456px;background:var(--tweet-blue)}
.tweets.charity{left:759px;background:var(--tweet-teal);color:#111}
.tweet{display:flex;gap:13px;padding-left:13px;height:83px;font-size:10.3px;line-height:17px}
.avatar{flex:none;width:45px;height:45px;background:var(--white);display:flex;align-items:center;justify-content:center;margin-top:2px}
.tweet b{font-weight:700}
.tweet-body{width:195px}
.bird{position:absolute;left:685px;top:10px;width:46px;height:56px;border-radius:50%;background:radial-gradient(circle at 40% 35%,#6fc6f2,#1f7fc4)}
/* footer */
.rule{position:absolute;left:154px;width:880px;height:1px;background:var(--rule)}
.link-col{position:absolute;top:376px;list-style:none;font-size:13.5px;line-height:28.2px}
.follow{position:absolute;left:903px;top:374px;font-family:"Ubuntu",sans-serif;font-weight:500;font-size:16px}
.social{position:absolute;left:904px;top:406px;display:flex;gap:6px}
.social span{width:28px;height:28px;border-radius:50%;background:var(--white)}
.brand{position:absolute;left:862px;top:455px;display:flex;align-items:center;gap:8px;font-family:"Ubuntu",sans-serif;font-weight:500;font-size:17px;line-height:17px;width:172px}
.brand i{flex:none;width:40px;height:40px;background:var(--white);transform:rotate(45deg) scale(.72)}
.copyright{position:absolute;top:540px;left:0;width:1188px;text-align:center;font-size:10px}
</style>
</head>
<body>
<h2 class="heading" style="left:153px">Latest Friendwall Feeds</h2>
<h2 class="heading" style="left:455px">Latest Tweets</h2>
<h2 class="heading" style="left:758px">Pet Charities Latest Tweets</h2>
<div class="bird" role="img" aria-label="Blue bird mascot illustration"></div>

<section class="panel fb">
  <div class="fb-head">Find us on Friendwall</div>
  <div class="fb-page">
    <span class="fb-mark"></span>
    <span class="fb-name">Pawline Platform</span>
    <span class="fb-like">&#128077; Like</span>
  </div>
  <p class="fb-count">2,147,179 people like <b>Pawline Platform</b>.</p>
  <div class="fb-grid">
    <div class="fb-fan"><span class="fb-thumb light" role="img" aria-label="Fan profile picture"></span>Samira</div>
    <div class="fb-fan"><span class="fb-thumb" role="img" aria-label="Fan profile picture"></span>Tarek</div>
    <div class="fb-fan"><span class="fb-thumb" role="img" aria-label="Fan profile picture"></span>Osvin</div>
    <div class="fb-fan"><span class="fb-thumb" role="img" aria-label="Fan profile picture"></span>Rafi</div>
    <div class="fb-fan"><span class="fb-thumb" role="img" aria-label="Fan profile picture"></span>Marisol</div>
    <div class="fb-fan"><span class="fb-thumb" role="img" aria-label="Fan profile picture"></span>Yusra</div>
    <div class="fb-fan"><span class="fb-thumb" role="img" aria-label="Fan profile picture"></span>Kenji</div>
    <div class="fb-fan"><span class="fb-thumb" role="img" aria-label="Fan profile picture"></span>Bora</div>
    <div class="fb-fan"><span class="fb-thumb" role="img" aria-label="Fan profile picture"></span>Idris</div>
    <div class="fb-fan"><span class="fb-thumb" role="img" aria-label="Fan profile picture"></span>Farouk</div>
  </div>
  <div class="fb-foot"><i></i>Friendwall social plugin</div>
</section>

<section class="panel tweets latest">
  <article class="tweet"><span class="avatar"><svg width="22" height="22" viewBox="0 0 22 22" fill="var(--avatar-icon-blue)"><circle cx="11" cy="7" r="5"/><path d="M1 21c0-6 4-8 10-8s10 2 10 8z"/></svg></span><p class="tweet-body"><b>Marnietolby</b> : Lorem ipsum dolor sit amet consecutor. Lorem ipsum dolor sit amet consecutor.<br>Wed,22 Apr 2013 22 : 33 : 08</p></article>
  <article class="tweet"><span class="avatar"><svg width="22" height="22" viewBox="0 0 22 22" fill="var(--avatar-icon-blue)"><circle cx="11" cy="7" r="5"/><path d="M1 21c0-6 4-8 10-8s10 2 10 8z"/></svg></span><p class="tweet-body"><b>Marnietolby</b> : Lorem ipsum dolor sit amet consecutor. Lorem ipsum dolor sit amet consecutor.<br>Wed,22 Apr 2013 22 : 33 : 08</p></article>
  <article class="tweet"><span class="avatar"><svg width="22" height="22" viewBox="0 0 22 22" fill="var(--avatar-icon-blue)"><circle cx="11" cy="7" r="5"/><path d="M1 21c0-6 4-8 10-8s10 2 10 8z"/></svg></span><p class="tweet-body"><b>Marnietolby</b> : Lorem ipsum dolor sit amet consecutor. Lorem ipsum dolor sit amet consecutor.<br>Wed,22 Apr 2013 22 : 33 : 08</p></article>
</section>

<section class="panel tweets charity">
  <article class="tweet"><span class="avatar"><svg width="22" height="22" viewBox="0 0 22 22" fill="var(--avatar-icon-teal)"><circle cx="11" cy="7" r="5"/><path d="M1 21c0-6 4-8 10-8s10 2 10 8z"/></svg></span><p class="tweet-body"><b>Marnietolby</b> : Lorem ipsum dolor sit amet consecutor. Lorem ipsum dolor sit amet consecutor.<br>Wed,22 Apr 2013 22 : 33 : 08</p></article>
  <article class="tweet"><span class="avatar"><svg width="22" height="22" viewBox="0 0 22 22" fill="var(--avatar-icon-teal)"><circle cx="11" cy="7" r="5"/><path d="M1 21c0-6 4-8 10-8s10 2 10 8z"/></svg></span><p class="tweet-body"><b>Marnietolby</b> : Lorem ipsum dolor sit amet consecutor. Lorem ipsum dolor sit amet consecutor.<br>Wed,22 Apr 2013 22 : 33 : 08</p></article>
  <article class="tweet"><span class="avatar"><svg width="22" height="22" viewBox="0 0 22 22" fill="var(--avatar-icon-teal)"><circle cx="11" cy="7" r="5"/><path d="M1 21c0-6 4-8 10-8s10 2 10 8z"/></svg></span><p class="tweet-body"><b>Marnietolby</b> : Lorem ipsum dolor sit amet consecutor. Lorem ipsum dolor sit amet consecutor.<br>Wed,22 Apr 2013 22 : 33 : 08</p></article>
</section>

<div class="rule" style="top:356px"></div>

<ul class="link-col" style="left:154px"><li>Link 1</li><li>Link 2</li><li>Link 3</li><li>Link 4</li><li>Link 5</li></ul>
<ul class="link-col" style="left:294px"><li>Link 1</li><li>Link 2</li><li>Link 3</li><li>Link 4</li><li>Link 5</li></ul>
<ul class="link-col" style="left:438px"><li>Link 1</li><li>Link 2</li><li>Link 3</li><li>Link 4</li><li>Link 5</li></ul>
<ul class="link-col" style="left:579px"><li>Link 1</li><li>Link 2</li><li>Link 3</li><li>Link 4</li><li>Link 5</li></ul>
<ul class="link-col" style="left:719px"><li>Link 1</li><li>Link 2</li><li>Link 3</li><li>Link 4</li><li>Link 5</li></ul>

<h3 class="follow">Follow Us On</h3>
<div class="social"><span></span><span></span><span></span><span></span></div>

<div class="brand"><i></i><span>Cover Compare Quizzo UK</span></div>

<div class="rule" style="top:525px"></div>
<p class="copyright">copyright 2013 © Cover Compare Quizzo UK</p>
</body>
</html>
```